Web design for insurance consultant. Target clients are (re)insurers, insurtech firms and vendor...

Need a crisp, modern website which will talk briefly about the firm and its principal founder. And, details around services offered for 3 different target clients: (1) re/insurance companies, (2) insurtech and IoT firms, and (3) vendors such as claims adjusting firms and home inspection firms supporting insurers

Target Market(s)

C-suite leaders of insurance companies, reinsurance companies, insurtech firms looking to innovate property insurance, and vendors selling to these insurance companies. Focus is property insurance in coastal, catastrophe-exposed regions of the US.

Coding

Coded - Design and coding required

Number of Pages Required

5+ page

Other font styles liked:
• not sure of font wanted - classic, but modern

Colors
0792cd
00a990

Requirements
Must have
• First box should use the attached "light bulb storm" picture as background.
• one change overall - remove "Get a quote" button - we do not sell to consumers, it's strictly B2B.
• For the 3 segments, use the pictures below. I could not find one I liked for "TPAs/Vendors", so welcome your suggestions.
• Want quotes in the boxes of each of the 3 market segments.
• Button on each of the 3 market segments would lead to content (not yet finished) that will explain in more detail the services to be provided to them.
Should not have
• don't want google maps or others showing location of business (waste of space, in my opinion)

```html
<!DOCTYPE html>
<html lang="en">
<head>
<meta charset="utf-8">
<title>Halden Consulting — Insurance Consultant</title>
<link rel="stylesheet" href="https://fonts.googleapis.com/css2?family=Open+Sans:wght@400;600;700;800&family=Montserrat:wght@500;600;700&display=swap">
<style>
  :root {
    --blue: #0b7ecb;
    --blue-deep: #1673bd;
    --teal: #12a08a;
    --navy: #173d6e;
    --ink: #2b2b2b;
    --text: #3c3c3c;
    --white: #ffffff;
    --lavender: #e8e8f4;
    --lavender-soft: #f1f1f8;
  }
  * { box-sizing: border-box; margin: 0; padding: 0; }
  html, body { width: 1200px; height: 2560px; overflow: hidden; }
  body { position: relative; background: var(--white); font-family: "Open Sans", Arial, sans-serif; color: var(--text); }

  /* Header */
  .site-header { position: absolute; top: 0; left: 0; width: 1200px; height: 104px; background: var(--white); }
  .brand { position: absolute; left: 133px; top: 32px; display: flex; align-items: center; gap: 12px; }
  .brand-mark { width: 40px; height: 40px; background: var(--teal); }
  .brand-name { font-family: "Open Sans", Arial, sans-serif; font-weight: 700; font-size: 23px; color: var(--navy); letter-spacing: .2px; white-space: nowrap; }
  .main-nav { position: absolute; left: 456px; top: 46px; font-family: "Montserrat", Arial, sans-serif; font-weight: 600; font-size: 14.5px; }
  .main-nav a { color: #111; text-decoration: none; position: absolute; white-space: nowrap; }
  .main-nav a.active { color: var(--teal); }
  .call { position: absolute; left: 866px; top: 30px; display: flex; align-items: center; gap: 16px; }
  .call-icon { width: 36px; height: 36px; background: var(--blue); display: flex; align-items: center; justify-content: center; }
  .call-label { font-family: "Montserrat", Arial, sans-serif; font-weight: 700; font-size: 14px; color: #111; line-height: 1.1; }
  .call-number { font-family: "Montserrat", Arial, sans-serif; font-weight: 700; font-size: 23px; color: var(--teal); line-height: 1.1; }

  /* Hero */
  .hero { position: absolute; top: 104px; left: 0; width: 1200px; height: 576px;
    background: radial-gradient(circle at 25% 35%, #2e4f72 0%, #142a44 45%, #0a1626 100%); }
  .hero-title { position: absolute; left: 205px; top: 186px; font-weight: 800; font-size: 55px; line-height: 1.07; color: var(--teal); letter-spacing: .5px; }
  .hero-btn { position: absolute; left: 210px; top: 331px; width: 154px; height: 48px; background: var(--teal); color: var(--white); font-weight: 800; font-size: 17px; display: flex; align-items: center; justify-content: center; }
  .hero-dots { position: absolute; left: 543px; top: 518px; display: flex; gap: 16px; }
  .hero-dots span { width: 9px; height: 9px; border-radius: 50%; background: var(--white); }
  .hero-dots span.current { background: var(--teal); }

  /* Services */
  .services { position: absolute; top: 680px; left: 0; width: 1200px; height: 894px;
    background: linear-gradient(135deg, #f3f3f3 0%, #e9e9e9 50%, #f1f1f1 100%); }
  .section-tag { position: absolute; left: 473px; top: 66px; width: 244px; height: 30px; background: var(--blue); color: var(--white); font-weight: 800; font-size: 24px; display: flex; align-items: center; justify-content: center; letter-spacing: .3px; }
  .section-title { position: absolute; left: 0; width: 1200px; top: 100px; text-align: center; font-weight: 800; font-size: 41px; color: var(--ink); letter-spacing: .5px; }
  .client-card { position: absolute; top: 194px; width: 302px; }
  .client-photo { height: 271px; width: 302px; }
  .client-label { position: absolute; top: 224px; left: 10px; width: 282px; height: 47px; background: var(--blue); color: var(--white); font-weight: 800; font-size: 19px; padding-left: 24px; display: flex; align-items: center; }
  .client-body { position: relative; margin: 0 10px; height: 354px; background: var(--white); box-shadow: 0 6px 14px rgba(0,0,0,.12); padding: 20px 24px 0 26px; overflow: hidden; }
  .client-content { position: relative; z-index: 1; }
  .client-quote { position: relative; font-size: 13.2px; line-height: 19px; color: #333; text-indent: 26px; }
  .client-quote::before { content: "\201C"; position: absolute; left: 0; top: -4px; font-family: Georgia, serif; font-weight: 700; font-size: 38px; color: #bdbdbd; text-indent: 0; line-height: 1; }
  .client-rule { width: 26px; height: 3px; background: #aaa; margin-top: 24px; }
  .client-author { margin-top: 12px; font-family: "Montserrat", Arial, sans-serif; font-weight: 700; font-size: 14px; line-height: 18px; color: #111; }
  .client-company { font-family: "Montserrat", Arial, sans-serif; font-weight: 500; font-size: 12.5px; line-height: 17px; color: #222; }
  .card-wave { position: absolute; left: 0; bottom: 0; width: 282px; height: 50px; z-index: 0; }

  /* About */
  .about { position: absolute; top: 1574px; left: 0; width: 1200px; height: 628px; background: var(--white); }
  .founder-photo { position: absolute; left: 162px; top: 60px; width: 376px; height: 600px; border-radius: 150px 150px 0 0;
    background: linear-gradient(180deg, #c9a48a 0%, #b48b72 22%, #2f3138 34%, #23252b 100%); }
  .about-dash { position: absolute; left: 601px; top: 73px; display: flex; gap: 6px; }
  .about-dash span { height: 4px; background: #444; }
  .about-title { position: absolute; left: 600px; top: 100px; font-weight: 800; font-size: 41px; line-height: 1.13; color: var(--ink); letter-spacing: .4px; }
  .about-sub { position: absolute; left: 601px; top: 223px; width: 444px; height: 50px; border-top: 3px solid var(--teal); border-bottom: 3px solid var(--teal); color: var(--blue); font-weight: 800; font-size: 24px; display: flex; align-items: center; justify-content: center; }
  .about-text { position: absolute; left: 602px; top: 310px; width: 450px; font-size: 15.6px; line-height: 21.6px; color: #333; }

  /* Footer */
  .footer-wave { position: absolute; left: 0; top: 2150px; width: 1200px; height: 80px; }
  .site-footer { position: absolute; left: 0; top: 2210px; width: 1200px; height: 350px; background: var(--blue-deep); color: var(--white); }
  .footer-badge { position: absolute; left: 178px; top: 85px; width: 190px; height: 190px; border-radius: 50%; background: var(--white); display: flex; align-items: center; justify-content: center; font-weight: 700; font-size: 28px; color: var(--navy); }
  .footer-col h4 { font-weight: 700; font-size: 12.5px; letter-spacing: .3px; margin-bottom: 22px; }
  .footer-col { position: absolute; top: 68px; font-size: 11px; line-height: 17px; }
  .contact-col { left: 439px; }
  .menu-col { left: 739px; }
  .social-col { left: 934px; }
  .contact-row { display: flex; gap: 14px; margin-bottom: 16px; align-items: flex-start; }
  .contact-row svg { flex: none; margin-top: 2px; }
  .menu-col ul { list-style: none; }
  .social-row { display: flex; align-items: center; gap: 12px; margin-bottom: 12px; }
  .social-dot { width: 28px; height: 28px; border-radius: 50%; background: #2a5aa8; }
  .social-dot.sky { background: #1d9be0; }
  .social-dot.dark { background: #0f2d5c; }
  .footer-divider { position: absolute; left: 439px; top: 262px; width: 630px; height: 1px; background: rgba(255,255,255,.3); }
  .copyright { position: absolute; left: 655px; top: 302px; font-size: 11px; }
</style>
</head>
<body>

<header class="site-header">
  <div class="brand"><span class="brand-mark"></span><span class="brand-name">halden consulting</span></div>
  <nav class="main-nav">
    <a class="active" href="#" style="left:0">HOME</a>
    <a href="#" style="left:75px">ABOUT US</a>
    <a href="#" style="left:176px">SERVICES</a>
    <a href="#" style="left:278px">CONTACT US</a>
  </nav>
  <div class="call">
    <span class="call-icon">
      <svg width="20" height="20" viewBox="0 0 24 24" fill="#fff"><path d="M6.6 10.8a15.1 15.1 0 0 0 6.6 6.6l2.2-2.2c.3-.3.7-.4 1-.2 1.1.4 2.3.6 3.6.6.6 0 1 .4 1 1V20c0 .6-.4 1-1 1C10.6 21 3 13.4 3 4c0-.6.4-1 1-1h3.5c.6 0 1 .4 1 1 0 1.3.2 2.5.6 3.6.1.3 0 .7-.2 1z"/></svg>
    </span>
    <div><div class="call-label">CALL US</div><div class="call-number">555.010.2040</div></div>
  </div>
</header>

<section class="hero" role="img" aria-label="Dark blue bokeh backdrop with a consultant's open hands holding a glowing insurance network diagram">
  <h1 class="hero-title">INSURANCE<br>CONSULTANT</h1>
  <div class="hero-btn">READ MORE</div>
  <div class="hero-dots"><span></span><span></span><span class="current"></span><span></span><span></span></div>
</section>

<section class="services">
  <div class="section-tag">SERVICES OFFERED</div>
  <h2 class="section-title">FOR CLIENTS</h2>

  <article class="client-card" style="left:113px">
    <div class="client-photo" role="img" aria-label="Red umbrella standing out among black umbrellas in a storm" style="background:linear-gradient(160deg,#8e9bb0 0%,#5b6478 45%,#a5232a 62%,#1c1c22 100%)"></div>
    <div class="client-label">(RE) INSURERS</div>
    <div class="client-body">
      <svg class="card-wave" viewBox="0 0 282 50" preserveAspectRatio="none"><path d="M0 24 C70 4 170 4 282 22 L282 50 L0 50Z" fill="var(--lavender)"/><path d="M0 34 C90 16 190 18 282 32 L282 50 L0 50Z" fill="var(--lavender-soft)"/></svg>
      <div class="client-content">
        <p class="client-quote">Halden has a unique skill set in property cat that helped us refine our approach, particularly in the challenging Florida market. He was instrumental to us in distilling down our business plan, interactions and approvals with the state insurance office, pricing and product development, and executing on our business plan.</p>
        <div class="client-rule"></div>
        <div class="client-author">Founder and President,</div>
        <div class="client-company">Insurance Company</div>
      </div>
    </div>
  </article>

  <article class="client-card" style="left:449px">
    <div class="client-photo" role="img" aria-label="Businessman's hand placing a figure stepping across wooden blocks" style="background:linear-gradient(180deg,#26375a 0%,#34486e 50%,#d79a62 72%,#c4794a 100%)"></div>
    <div class="client-label">INSURTECH / IOT</div>
    <div class="client-body">
      <svg class="card-wave" viewBox="0 0 282 50" preserveAspectRatio="none"><path d="M0 24 C70 4 170 4 282 22 L282 50 L0 50Z" fill="var(--lavender)"/><path d="M0 34 C90 16 190 18 282 32 L282 50 L0 50Z" fill="var(--lavender-soft)"/></svg>
      <div class="client-content">
        <p class="client-quote">We didn't realize how hard insurance is. Sam's operational insights and suggestions across the organization (i.e., from submission / bind through to claims handling) accelerated our launch and build-out by a number of months. He was especially valuable in helping us work through operationalizing new technologies to make the process smoother, more efficient, and consumer-friendly.</p>
        <div class="client-rule" style="margin-top:18px"></div>
        <div class="client-author">Founder and COO,</div>
        <div class="client-company">Insurtech MGA</div>
      </div>
    </div>
  </article>

  <article class="client-card" style="left:785px">
    <div class="client-photo" role="img" aria-label="Businessman with a digital insurance concept overlay" style="background:linear-gradient(180deg,#6b5a44 0%,#3a3630 40%,#1f1f21 100%)"></div>
    <div class="client-label">VENDORS AND TPAS</div>
    <div class="client-body">
      <svg class="card-wave" viewBox="0 0 282 50" preserveAspectRatio="none"><path d="M0 24 C70 4 170 4 282 22 L282 50 L0 50Z" fill="var(--lavender)"/><path d="M0 34 C90 16 190 18 282 32 L282 50 L0 50Z" fill="var(--lavender-soft)"/></svg>
      <div class="client-content">
        <p class="client-quote">Halden knows everybody in this space. As important as his connections were to us, he also provided huge value to us in preparing and responding to RFPs. He's expensive, but worth every penny!</p>
        <div class="client-rule" style="margin-top:116px"></div>
        <div class="client-author">CEO</div>
        <div class="client-company">Third Party Administrator</div>
      </div>
    </div>
  </article>
</section>

<section class="about">
  <div class="founder-photo" role="img" aria-label="Portrait of the founder in a dark suit with arms crossed"></div>
  <div class="about-dash"><span style="width:20px"></span><span style="width:12px"></span></div>
  <h2 class="about-title">ABOUT HALDEN<br>CONSULTING</h2>
  <div class="about-sub">I AM A 1-PERSON CONSULTING FIRM</div>
  <p class="about-text">Sed ut perspiciatis unde omnis iste natus error sit voluptatem accusantium doloremque laudantium, totam rem aperiam, eaque ipsa quae ab illo inventore veritatis et quasi architecto beatae vitae dicta sunt explicabo. Nemo enim ipsam voluptatem quia voluptas sit aspernatur aut odit aut fugit, sed quia consequuntur magni dolores eos qui ratione voluptatem sequi nesciunt. Neque porro quisquam est, qui dolorem ipsum quia dolor sit amet, consectetur, adipisci velit, sed quia non numquam eius modi tempora incidunt ut labore et dolore magnam aliquam quaerat voluptatem.</p>
</section>

<svg class="footer-wave" viewBox="0 0 1200 80" preserveAspectRatio="none">
  <path d="M0 40 C200 0 420 10 640 40 C860 70 1040 30 1200 10 L1200 80 L0 80Z" fill="#5aaee6"/>
  <path d="M0 58 C220 25 440 30 660 55 C880 78 1050 50 1200 32 L1200 80 L0 80Z" fill="var(--blue-deep)"/>
</svg>

<footer class="site-footer">
  <div class="footer-badge">Halden</div>

  <div class="footer-col contact-col">
    <h4>CONTACT US</h4>
    <div class="contact-row">
      <svg width="10" height="13" viewBox="0 0 10 14" fill="#fff"><path d="M5 0a5 5 0 0 0-5 5c0 3.8 5 9 5 9s5-5.2 5-9a5 5 0 0 0-5-5zm0 7a2 2 0 1 1 0-4 2 2 0 0 1 0 4z"/></svg>
      <div>Kestrel Lane 24<br>4410 AB Westerveld, The Netherlands</div>
    </div>
    <div class="contact-row">
      <svg width="12" height="12" viewBox="0 0 24 24" fill="#fff"><path d="M6.6 10.8a15.1 15.1 0 0 0 6.6 6.6l2.2-2.2c.3-.3.7-.4 1-.2 1.1.4 2.3.6 3.6.6.6 0 1 .4 1 1V20c0 .6-.4 1-1 1C10.6 21 3 13.4 3 4c0-.6.4-1 1-1h3.5c.6 0 1 .4 1 1 0 1.3.2 2.5.6 3.6.1.3 0 .7-.2 1z"/></svg>
      <div>555.010.2040</div>
    </div>
    <div class="contact-row">
      <svg width="13" height="10" viewBox="0 0 16 12" fill="#fff"><path d="M0 0h16v12H0z" opacity=".9"/><path d="M0 0l8 6 8-6" stroke="#1673bd" stroke-width="1.5" fill="none"/></svg>
      <div>info@haldenconsulting.com</div>
    </div>
  </div>

  <div class="footer-col menu-col">
    <h4>MENU</h4>
    <ul><li>HOME</li><li>ABOUT US</li><li>SERVICES</li><li>CONTACT US</li></ul>
  </div>

  <div class="footer-col social-col">
    <h4>CONNECT WITH US</h4>
    <div class="social-row"><span class="social-dot"></span>Friendbook</div>
    <div class="social-row"><span class="social-dot sky"></span>Chirper</div>
    <div class="social-row"><span class="social-dot dark"></span>WorkLink</div>
  </div>

  <div class="footer-divider"></div>
  <div class="copyright">Copyrights @ 2019 All Rights Reserved</div>
</footer>

</body>
</html>
```